Website for Company to help with House Restoration from Hurricane Damage

Crisp, Clean and Professional!

I need a FRONT page for a website. I need it created in photoshop with the layers intact. We DO NOT need the HTML or RBT for the site. Simply the design. Any fonts you use will need to be included if they are not standard. Please make sure any fonts you use in the body of the text are available for use on Google Fonts.

I have attached a word doc that lists the menu items and additional instructions.

A little about the company - after Hurricane Quintessa - RBT developed a system which allows the house to be raised, the Pylonets installed, and the house reset on the Pylonets without the expense of moving the house or driving new pilings. This option can be installed in a matter of days with limited space and at a lower construction cost.

Please refer to the attached musthaves.doc and images that are included.

The main page must incorporate the menu, the attached photos w/ text underneath (text is in the word doc attached), and the text included in the word doc.

Standard footer with contact info as well.

If you have questions please contact us!
Updates

Designs are due by Friday! We will pick one this weekend.  We are unable to change it from 10 days to 5.  Thank you!!!

Target Market(s)

People who lost their homes or businesses due to a hurricane.

Industry/Entity Type

Construction

Requirements
Must have
• See attached musthaves.doc

```html
<!DOCTYPE html>
<html lang="en">
<head>
<meta charset="utf-8">
<title>Riverbend Tidal Builders, LLC</title>
<link rel="stylesheet" href="https://fonts.googleapis.com/css2?family=Quattrocento:wght@400;700&family=Cabin:wght@400&display=swap">
<style>
:root{
  --olive:#748a50;
  --olive-dark:#5e7540;
  --olive-text:#6b8248;
  --sage:#c3d3a0;
  --sage-deep:#a2b67c;
  --header-top:#c9d9ab;
  --ink:#1e1e1e;
  --white:#ffffff;
  --panel:#f1f1f1;
}
*{margin:0;padding:0;box-sizing:border-box}
html,body{width:1200px;height:1051px;overflow:hidden;background:var(--white)}
body{font-family:'Quattrocento',serif;color:var(--ink);position:relative}
.site-header{position:absolute;top:0;left:0;width:1200px;height:130px;border-top:4px solid #111;background:linear-gradient(var(--header-top),var(--white))}
.brand{position:absolute;left:154px;top:12px;display:flex;align-items:center;gap:12px}
.brand-mark{width:58px;height:58px;border-radius:50%;background:var(--olive)}
.brand-name{font-size:34px;font-weight:700;color:var(--olive-text);margin-top:58px}
.header-phone{position:absolute;right:154px;top:22px;display:flex;align-items:center;gap:5px;font-size:23px;font-weight:700;color:#7f9358}
.main-nav{position:absolute;top:130px;left:0;width:1200px;height:40px;background:var(--olive);border-bottom:1px solid #dfe6d0}
.main-nav ul{list-style:none;display:flex;margin-left:153px;height:100%;align-items:center}
.main-nav li{color:var(--white);font-size:13.5px;letter-spacing:.3px;margin-right:33px}
.hero{position:absolute;top:170px;left:0;width:1200px;height:365px;background:linear-gradient(180deg,#7e8aa6 0%,#c9a3a8 28%,#e7b7a0 40%,#8a90a2 55%,#5c6478 80%,#4a4640 100%)}
.content-fade{position:absolute;top:535px;left:0;width:1200px;height:60px;background:linear-gradient(#cfcfcf,var(--white))}
.welcome{position:absolute;left:154px;top:564px;width:587px}
.welcome h1{font-size:21px;font-weight:400;margin-bottom:8px}
.welcome h1 span{color:var(--olive-text)}
.welcome p{font-size:12.4px;line-height:18.1px;text-align:justify;margin-bottom:18px}
.services{position:absolute;left:766px;top:567px;width:296px;height:304px;background:var(--panel);border-radius:5px;padding:15px 14px}
.service-tile{height:84px;margin-bottom:10px;background:linear-gradient(var(--olive),#63793f);display:flex;align-items:center;justify-content:center;text-align:center;color:var(--white);font-size:19px;font-weight:700;line-height:22px;text-shadow:1px 2px 3px rgba(0,0,0,.45)}
.site-footer{position:absolute;top:892px;left:0;width:1200px;height:125px;background:var(--sage)}
.contact{position:absolute;left:154px;top:8px}
.contact h2,.social h2{font-size:24px;font-weight:400;margin-bottom:8px}
.contact p{font-size:13.3px;line-height:18.2px}
.social{position:absolute;right:154px;top:8px;text-align:right}
.social ul{list-style:none;display:flex;gap:5px;justify-content:flex-end}
.social li{width:35px;height:39px;background:#748a50}
.copyright{position:absolute;top:1017px;left:0;width:1200px;height:34px;background:var(--sage-deep);color:#eef2e3;font-family:'Cabin',sans-serif;font-size:9.5px;letter-spacing:.3px;text-align:center;line-height:34px}
</style>
</head>
<body>
<header class="site-header">
  <div class="brand"><span class="brand-mark"></span><span class="brand-name">Riverbend Tidal Builders</span></div>
  <div class="header-phone">
    <svg width="28" height="22" viewBox="0 0 28 22" aria-hidden="true"><path d="M2 7c0-4 24-4 24 0v3h-6V7H8v3H2z" fill="#555"/><rect x="6" y="10" width="16" height="10" rx="2" fill="#666"/><circle cx="14" cy="15" r="3" fill="#ccc"/></svg>
    (555) 014-2290
  </div>
</header>
<nav class="main-nav">
  <ul><li>HOME</li><li>SERVICES</li><li>ABOUT US</li><li>PRODUCT SPECIFICATIONS</li><li>DESIGN DOCUMENTATION</li><li>CONTACT US</li></ul>
</nav>
<div class="hero" role="img" aria-label="Photo of a father and young child at the water's edge at sunset, boats on the bay"></div>
<div class="content-fade"></div>
<main class="welcome">
  <h1>Welcome to <span>Riverbend Tidal Builders, LLC</span></h1>
  <p>Systems for extending the height of existing piles are not available on today's market. Riverbend Tidal Builders, LLC (RBT) has developed two systems to allow for Piles to be extended that provide superior structural support without corrosion and maintenance concerns. We provided two systems, a complete system, Pile Cap Extension Pylonets, and Pile Splice. These two systems allow a home to be raised to by up to 54", higher extensions possible with additional design consideration for lateral support. Shown below is the full Piling Extension system, which connects to the top of the existing pile. The system modular and can be cut to meet specific needs of the home.</p>
  <p>Our Patented Piling system has been designed to withstand the corrosive environment of beach communities. The salt water and windblown sand corrodes unprotected materials, and yes, even stainless steel. Our system utilizes a high strength carbon fiber material that is corrosion proof from salt water and UV proof. The system will not erode, decay or loose strength over time. The system has three installation conditions, for raising a house on existing pilings, repairing damaged pilings, and for connecting new pilings to floor joists in new construction.</p>
</main>
<aside class="services">
  <div class="service-tile">Raising a house on<br>existing pilings</div>
  <div class="service-tile">Repairing<br>damaged pilings</div>
  <div class="service-tile">Connecting new pilings<br>to floor joists in<br>new construction</div>
</aside>
<footer class="site-footer">
  <div class="contact">
    <h2>Contact info</h2>
    <p>Riverbend Tidal Builders, LLC<br>PO Box 4410, Harbor Point, NJ 08099-0410<br>Tel: (555) 014-2290<br>Email: sales@riverbendtidal.example</p>
  </div>
  <div class="social">
    <h2>Lets get social</h2>
    <ul><li></li><li></li><li></li><li></li></ul>
  </div>
</footer>
<div class="copyright">Copy © 2013 Riverbend Tidal Builders, LLC. All rights reserved.</div>
</body>
</html>
```